Business card design needed

Marketing Communications

Target Market(s)

prospective clients in the marketing communications industry

Industry/Entity Type

Business

Contact Information for Business Card

merel vasko
Marketing Communications
tolupar@quennet.com
0462 815947

Logo Text

merel vasko

Logo styles of interest
Abstract Logo
Requirements
Must have
• An appropriate abstract logo. only a one or two colour design
Nice to have
• Logo to portray the growth of a marketing brief
Should not have
• no more than two colours maximum

```html
<!DOCTYPE html>
<html lang="en">
<head>
<meta charset="utf-8">
<title>Merel Vasko – Business Card</title>
<link rel="stylesheet" href="https://fonts.googleapis.com/css2?family=Cormorant+SC:wght@700&family=Noto+Sans+Mono:wght@400;600&display=swap">
<style>
  :root {
    --frame-outer: #e00000;
    --frame-inner: #33f0ff;
    --panel-upper: #c0cdcb;
    --panel-lower-a: #b4c1c1;
    --panel-lower-b: #bcc8c8;
    --ink: #111111;
    --mark: #2f6fd8;
  }
  html, body {
    margin: 0;
    padding: 0;
    overflow: hidden;
    background: #ffffff;
  }
  .card {
    position: relative;
    width: 1200px;
    height: 695px;
    background: var(--frame-outer);
    overflow: hidden;
  }
  .card__frame {
    position: absolute;
    left: 20px;
    top: 14px;
    width: 1160px;
    height: 665px;
    background: var(--frame-inner);
  }
  .card__panel {
    position: absolute;
    left: 43px;
    top: 36px;
    width: 1116px;
    height: 621px;
    background: var(--panel-upper);
    overflow: hidden;
  }
  .card__panel svg {
    position: absolute;
    left: 0;
    top: 0;
  }
  .brand {
    position: absolute;
    left: 86px;
    top: 62px;
    display: flex;
    align-items: center;
    gap: 26px;
  }
  .brand__mark {
    width: 100px;
    height: 100px;
    background: var(--mark);
  }
  .brand__name {
    font-family: "Noto Sans Mono", monospace;
    font-weight: 600;
    font-size: 42px;
    color: var(--ink);
    letter-spacing: 0;
  }
  .contact {
    position: absolute;
    left: 560px;
    top: 352px;
    width: 620px;
    text-align: center;
    color: var(--ink);
  }
  .contact__name {
    font-family: "Cormorant SC", serif;
    font-weight: 700;
    font-size: 54px;
    line-height: 60px;
    margin: 0 0 2px;
    text-transform: capitalize;
  }
  .contact__line {
    font-family: "Noto Sans Mono", monospace;
    font-weight: 400;
    font-size: 33px;
    line-height: 47px;
    margin: 0;
  }
</style>
</head>
<body>
  <div class="card">
    <div class="card__frame"></div>
    <div class="card__panel">
      <svg width="1116" height="621" viewBox="0 0 1116 621" role="img" aria-label="Woven fabric texture filling the lower diagonal half of the card">
        <defs>
          <linearGradient id="fabric-tone" x1="0" y1="1" x2="1" y2="0">
            <stop offset="0" stop-color="var(--panel-lower-a)"/>
            <stop offset="1" stop-color="var(--panel-lower-b)"/>
          </linearGradient>
        </defs>
        <polygon points="0,547 1044,0 1116,0 1116,621 0,621" fill="url(#fabric-tone)"/>
      </svg>
    </div>

    <div class="brand">
      <div class="brand__mark"></div>
      <div class="brand__name">Marketing Communications</div>
    </div>

    <div class="contact">
      <p class="contact__name">merel vasko</p>
      <p class="contact__line">Marketing Communications</p>
      <p class="contact__line">0462-815947</p>
      <p class="contact__line">tolupar@quennet.com</p>
    </div>
  </div>
</body>
</html>
```